re-skin an existing app using new logo and color scheme

The company that created the existing app TotNest will be re-skinning the app on our behalf. We need to get a design submitted to them that retains the same functionality of their app but using our brand's look and feel. The product this app will be used in conjunction with is called Vero Band.
Vero Band is a stand-alone cellular watch that allows anyone from kids to seniors to make phone calls by simply pushing one of four buttons on the watch. The SOS button connects you to a live team of emergency professionals that can patch you to a 911 operator. Two of the other buttons are programmable to dial any desired phone number. The fourth button (called the "Magic" button) connects you with a live team of personal assistants that can help you with anything you want, including transferring you to any number, making dinner reservations, answering trivia, finding movie times and anything else you can imagine.
The built-in GPS functionality of the watch allows you to track the location of the watch at any time from the Vero Band website or the Vero Band app. You can also set up a perimeter around a specific area so that you can receive alerts when the watch travels outside of the "geofence".
Our slogan is: "Always safe on our watch"
We have included in the materials the Vero Band logo (in Adobe Illustrator). We have also included screen shots of some of the screens of the existing app (TotNest).
Using our logo, please design a re-skin of the attached screen shots. We want a simple, clean design. A great example of this is the Spot-o-Trek app:
https://www.portfoliyo.example/gallery/Spot-o-Trek/5927143
For the login redesign, this can be redone as far as the placement of the fields and buttons etc. Please make sure to include the slogan "Always safe on our watch" somewhere on the login screen.
For the navigation screen, only the top part will be available for you to redesign - the bottom 80% of the screen needs to stay the same. (where it says "Device name: Teal Band" and below)
For the privilege screen, this can be completely redesigned.
For the family numbers setting screen, this can be completely redesigned.
For the whitelist setting screen, this can be completely redesigned.
Any questions, let us know.

```html
<!DOCTYPE html>
<html lang="en">
<head>
<meta charset="utf-8">
<title>Whitelist Setting</title>
<link href="https://fonts.googleapis.com/css2?family=Montserrat:wght@600;700&family=Questrial&display=swap" rel="stylesheet">
<style>
  :root {
    --brand: #5ed3ef;
    --page: #f3f3f3;
    --field: #e0e0e0;
    --field-border: #555555;
    --ink: #444444;
    --icon: #4a4a4a;
    --placeholder: #c2c2c2;
    --slot-idle: #e2e2e2;
    --divider: #c8c8c8;
    --white: #ffffff;
  }
  * { box-sizing: border-box; margin: 0; padding: 0; }
  html, body { width: 1200px; height: 2746px; overflow: hidden; background: var(--page); }
  .screen { position: relative; width: 1200px; height: 2746px; background: var(--page); overflow: hidden; }

  .app-header { position: absolute; left: 0; top: 0; width: 1200px; height: 275px; background: var(--brand); color: var(--white); }
  .status-bar { position: absolute; left: 0; top: 28px; width: 1200px; height: 55px; font-family: "Questrial", sans-serif; font-size: 37px; }
  .status-bar .signal { position: absolute; left: 40px; top: 12px; display: flex; gap: 7px; }
  .status-bar .signal span { width: 30px; height: 30px; border-radius: 50%; border: 3px solid var(--white); }
  .status-bar .signal span.on { background: var(--white); }
  .status-bar .carrier { position: absolute; left: 272px; top: 5px; }
  .status-bar .wifi { position: absolute; left: 418px; top: 6px; }
  .status-bar .clock { position: absolute; left: 542px; top: 5px; }
  .status-bar .indicators { position: absolute; left: 756px; top: 4px; display: flex; gap: 14px; align-items: center; }
  .status-bar .charge { position: absolute; left: 952px; top: 5px; display: flex; align-items: center; gap: 10px; }
  .battery { width: 62px; height: 28px; border: 3px solid var(--white); border-radius: 5px; position: relative; padding: 3px; }
  .battery::before { content: ""; display: block; width: 100%; height: 100%; background: var(--white); border-radius: 2px; }
  .battery::after { content: ""; position: absolute; right: -9px; top: 7px; width: 5px; height: 10px; background: var(--white); border-radius: 0 2px 2px 0; }

  .back-button { position: absolute; left: 52px; top: 150px; }
  .screen-title { position: absolute; left: 150px; top: 143px; font-family: "Montserrat", sans-serif; font-weight: 600; font-size: 56px; letter-spacing: 1px; line-height: 70px; }

  .whitelist { position: absolute; left: 0; top: 343px; width: 1200px; list-style: none; }
  .entry { position: relative; height: 304px; }
  .entry::after { content: ""; position: absolute; left: 148px; top: 263px; width: 933px; height: 3px; background: var(--divider); }
  .entry:last-child::after { display: none; }
  .slot { position: absolute; left: 148px; top: 0; width: 145px; height: 207px; border-radius: 30px; background: var(--slot-idle); color: var(--ink); font-family: "Montserrat", sans-serif; font-weight: 700; font-size: 72px; display: flex; align-items: center; justify-content: center; }
  .entry.is-filled .slot { background: var(--brand); color: var(--white); }
  .field-icon { position: absolute; left: 366px; width: 92px; height: 92px; }
  .field-icon.person { top: -2px; }
  .field-icon.phone { top: 114px; }
  .field { position: absolute; left: 496px; width: 545px; height: 88px; border: 4px solid var(--field-border); border-radius: 18px; background: var(--field); font-family: "Questrial", sans-serif; font-size: 54px; color: var(--ink); padding-left: 24px; line-height: 80px; white-space: nowrap; overflow: hidden; }
  .field.name { top: 0; }
  .field.number { top: 117px; }
  .field.empty { color: var(--placeholder); }
</style>
</head>
<body>
<svg width="0" height="0" style="position:absolute" aria-hidden="true">
  <defs>
    <symbol id="icon-person" viewBox="0 0 92 92">
      <circle cx="46" cy="46" r="46" fill="#4a4a4a"/>
      <circle cx="46" cy="35" r="15" fill="#ffffff"/>
      <path d="M20 70 Q20 52 46 52 Q72 52 72 70 Z" fill="#ffffff"/>
    </symbol>
    <symbol id="icon-phone" viewBox="0 0 92 92">
      <circle cx="46" cy="46" r="46" fill="#4a4a4a"/>
      <path transform="translate(73.6 18.4) scale(-2.3 2.3)" fill="#ffffff" d="M6.62 10.79c1.44 2.83 3.76 5.14 6.59 6.59l2.2-2.2c.27-.27.67-.36 1.02-.24 1.12.37 2.33.57 3.57.57.55 0 1 .45 1 1V20c0 .55-.45 1-1 1-9.39 0-17-7.61-17-17 0-.55.45-1 1-1h3.5c.55 0 1 .45 1 1 0 1.25.2 2.45.57 3.57.11.35.03.74-.25 1.02l-2.2 2.2z"/>
    </symbol>
  </defs>
</svg>

<main class="screen">
  <header class="app-header">
    <div class="status-bar">
      <div class="signal"><span class="on"></span><span class="on"></span><span class="on"></span><span></span><span></span></div>
      <span class="carrier">Vireo</span>
      <svg class="wifi" width="56" height="42" viewBox="0 0 56 42" aria-hidden="true">
        <path d="M2 14 Q28 -8 54 14 L47 21 Q28 5 9 21 Z M14 26 Q28 14 42 26 L35 33 Q28 27 21 33 Z M28 42 L23 37 Q28 33 33 37 Z" fill="#ffffff"/>
      </svg>
      <span class="clock">2:42 PM</span>
      <div class="indicators" aria-hidden="true">
        <svg width="36" height="36" viewBox="0 0 36 36"><path d="M34 2 L2 16 L18 18 L20 34 Z" fill="#ffffff"/></svg>
        <svg width="40" height="40" viewBox="0 0 40 40"><circle cx="20" cy="22" r="15" fill="#ffffff"/><circle cx="7" cy="7" r="5" fill="#ffffff"/><circle cx="33" cy="7" r="5" fill="#ffffff"/><path d="M20 13 V22 H27" stroke="#5ed3ef" stroke-width="3" fill="none"/></svg>
        <svg width="24" height="40" viewBox="0 0 24 40"><path d="M3 11 L20 28 L11 36 V4 L20 12 L3 29" stroke="#ffffff" stroke-width="3" fill="none"/></svg>
      </div>
      <div class="charge">
        <span>100%</span>
        <span class="battery"></span>
        <svg width="18" height="30" viewBox="0 0 18 30" aria-hidden="true"><path d="M11 0 L2 17 H9 L6 30 L16 12 H9 Z" fill="#ffffff"/></svg>
      </div>
    </div>
    <svg class="back-button" width="42" height="58" viewBox="0 0 42 58" aria-label="Back" role="img">
      <path d="M40 0 V58 L0 29 Z" fill="#ffffff"/>
    </svg>
    <h1 class="screen-title">WHITELIST SETTING</h1>
  </header>

  <ol class="whitelist">
    <li class="entry is-filled">
      <div class="slot">1</div>
      <svg class="field-icon person"><use href="#icon-person"/></svg>
      <svg class="field-icon phone"><use href="#icon-phone"/></svg>
      <div class="field name">Sam Rivera</div>
      <div class="field number">1-620-555-148</div>
    </li>
    <li class="entry is-filled">
      <div class="slot">2</div>
      <svg class="field-icon person"><use href="#icon-person"/></svg>
      <svg class="field-icon phone"><use href="#icon-phone"/></svg>
      <div class="field name">Lena Park</div>
      <div class="field number">1-731-555-192</div>
    </li>
    <li class="entry">
      <div class="slot">3</div>
      <svg class="field-icon person"><use href="#icon-person"/></svg>
      <svg class="field-icon phone"><use href="#icon-phone"/></svg>
      <div class="field name empty">Name</div>
      <div class="field number empty">Phone Number</div>
    </li>
    <li class="entry">
      <div class="slot">4</div>
      <svg class="field-icon person"><use href="#icon-person"/></svg>
      <svg class="field-icon phone"><use href="#icon-phone"/></svg>
      <div class="field name empty">Name</div>
      <div class="field number empty">Phone Number</div>
    </li>
    <li class="entry">
      <div class="slot">5</div>
      <svg class="field-icon person"><use href="#icon-person"/></svg>
      <svg class="field-icon phone"><use href="#icon-phone"/></svg>
      <div class="field name empty">Name</div>
      <div class="field number empty">Phone Number</div>
    </li>
    <li class="entry">
      <div class="slot">6</div>
      <svg class="field-icon person"><use href="#icon-person"/></svg>
      <svg class="field-icon phone"><use href="#icon-phone"/></svg>
      <div class="field name empty">Name</div>
      <div class="field number empty">Phone Number</div>
    </li>
    <li class="entry">
      <div class="slot">7</div>
      <svg class="field-icon person"><use href="#icon-person"/></svg>
      <svg class="field-icon phone"><use href="#icon-phone"/></svg>
      <div class="field name empty">Name</div>
      <div class="field number empty">Phone Number</div>
    </li>
    <li class="entry">
      <div class="slot">8</div>
      <svg class="field-icon person"><use href="#icon-person"/></svg>
      <svg class="field-icon phone"><use href="#icon-phone"/></svg>
      <div class="field name empty">Name</div>
      <div class="field number empty">Phone Number</div>
    </li>
  </ol>
</main>
</body>
</html>
```